Business card for Sports Apparel business

DOUBLE SIDED DESIGN
We need business cards for a new sports apparel business. We are developing a protective headband for soccer initially.
Corvell is focused on designing and developing head protection products to reduce the likelihood of concussion when playing sports. Exploring and understanding medical insights, material science research, current and former players experiences and governing bodies guidelines has allowed Corvell to develop the safety, style, form and function requirements of a suitable product to bring to market.
Target Market(s)
Mums buying kits for the sons and daughters. Amateur footballers.
Industry/Entity Type
Sporting Good
Contact Information for Business Card
Martin Ashgrove - CEO
Mobile: +44 7391608254
Email: martin@corvell.co.uk
Tel: 0208 5143927
Helena Pardoe - COO
Mob: +44 7356 409183
Email: helena@corvell.co.uk
Tel: 0208 5143927
Duncan Wyvern - CCO
Mob: +44 7468 230517
Email: duncan@corvell.co.uk
Tel: 0208 5143927
Look and feel

```html
<!DOCTYPE html>
<html lang="en">
<head>
<meta charset="utf-8">
<title>Corvell Business Card</title>
<link rel="stylesheet" href="https://fonts.googleapis.com/css2?family=Montserrat:wght@500;700&family=Arimo:wght@400&display=swap">
<style>
  :root {
    --bg: #2f2f2f;
    --card-white: #ffffff;
    --card-grey: #666666;
    --brand-blue: #0a5a94;
    --rule-blue: #8fb4d4;
    --text-dark: #222222;
    --text-grey: #555555;
  }
  * { box-sizing: border-box; margin: 0; padding: 0; }
  html, body { width: 1200px; height: 866px; overflow: hidden; }
  body {
    background: var(--bg);
    display: flex;
    align-items: center;
    justify-content: center;
    gap: 50px;
  }
  .card {
    position: relative;
    width: 540px;
    height: 340px;
    overflow: hidden;
    box-shadow: 0 10px 30px rgba(0,0,0,0.45);
  }
  .card--front { background: var(--card-white); }
  .card--back {
    background: var(--card-grey);
    display: flex;
    align-items: center;
    justify-content: center;
  }
  .brand-name {
    font-family: "Montserrat", sans-serif;
    font-weight: 700;
    letter-spacing: 4px;
    text-transform: uppercase;
    display: flex;
    align-items: center;
    gap: 12px;
  }
  .brand-name::before {
    content: "";
    width: 0.55em;
    height: 0.55em;
    background: currentColor;
    display: block;
  }
  .card--front .brand-name {
    position: absolute;
    right: 38px;
    top: 112px;
    font-size: 40px;
    color: var(--brand-blue);
  }
  .card--back .brand-name {
    font-size: 50px;
    color: var(--card-white);
  }
  .contact-block {
    position: absolute;
    left: 38px;
    top: 180px;
  }
  .person-name {
    font-family: "Montserrat", sans-serif;
    font-weight: 700;
    font-size: 17px;
    color: var(--brand-blue);
    text-transform: uppercase;
    letter-spacing: 0.5px;
  }
  .person-role {
    font-family: "Arimo", sans-serif;
    font-size: 13px;
    color: var(--text-grey);
    margin-bottom: 10px;
  }
  .contact-list { list-style: none; }
  .contact-list li {
    display: flex;
    align-items: center;
    gap: 10px;
    font-family: "Arimo", sans-serif;
    font-size: 13.5px;
    color: var(--text-dark);
    line-height: 21px;
  }
  .contact-icon { width: 16px; height: 16px; flex: none; }
  .rule {
    position: absolute;
    left: 220px;
    right: 38px;
    top: 198px;
    height: 1px;
    background: var(--rule-blue);
  }
  .band {
    position: absolute;
    bottom: 0;
    height: 10px;
  }
  .band--blue { left: 0; width: 56%; background: var(--brand-blue); }
  .band--grey { right: 0; width: 44%; background: var(--card-grey); height: 14px; }
</style>
</head>
<body>
  <section class="card card--front" aria-label="Card front">
    <div class="brand-name">Corvell</div>
    <div class="rule"></div>
    <div class="contact-block">
      <p class="person-name">Martin Ashgrove</p>
      <p class="person-role">CEO</p>
      <ul class="contact-list">
        <li>
          <svg class="contact-icon" viewBox="0 0 16 16" aria-hidden="true">
            <rect x="0.75" y="0.75" width="14.5" height="14.5" fill="none" stroke="#0a5a94" stroke-width="1.5"/>
            <path d="M5 4 L6.5 4 L7.3 6 L6.3 6.8 Q7.2 8.8 9.2 9.7 L10 8.7 L12 9.5 L12 11 Q8 11.5 5.2 8.5 Q4 6.5 5 4 Z" fill="#0a5a94"/>
          </svg>
          0208 5143927
        </li>
        <li>
          <svg class="contact-icon" viewBox="0 0 16 16" aria-hidden="true">
            <rect x="0.75" y="0.75" width="14.5" height="14.5" fill="none" stroke="#0a5a94" stroke-width="1.5"/>
            <rect x="5.5" y="3" width="5" height="10" rx="1" fill="none" stroke="#0a5a94" stroke-width="1.2"/>
            <circle cx="8" cy="11.3" r="0.7" fill="#0a5a94"/>
          </svg>
          +44 7391608254
        </li>
        <li>
          <svg class="contact-icon" viewBox="0 0 16 16" aria-hidden="true">
            <rect x="0.75" y="0.75" width="14.5" height="14.5" fill="none" stroke="#0a5a94" stroke-width="1.5"/>
            <rect x="3.5" y="4.5" width="9" height="7" fill="none" stroke="#0a5a94" stroke-width="1.2"/>
            <path d="M3.5 4.5 L8 8.5 L12.5 4.5" fill="none" stroke="#0a5a94" stroke-width="1.2"/>
          </svg>
          martin@corvell.co.uk
        </li>
      </ul>
    </div>
    <div class="band band--blue"></div>
    <div class="band band--grey"></div>
  </section>

  <section class="card card--back" aria-label="Card back">
    <div class="brand-name">Corvell</div>
  </section>
</body>
</html>
```